Brochure Design for Finance Company

We are looking for 2 double-sided A4 brochures.
We are a Scandinavian finance company now operating in Australia. The main service we provide, and which the brochures are for, is Invoice Factoring. While invoice factoring isn’t new, the way we let our clients factor their invoices is. We have simply made Invoice Factoring simple, and we need the brochures to reflect that.
Brochure 1: Why Invoice Factoring
This brochure is meant for potential clients who have never heard of Invoice Factoring before. It should communicate business growth and speeding up cash flow.
Brochure 2: Why Us
This brochure explains how our service differs from our competitors. It should communicate how simple and easy it is to use our service.
We aim to be seen as professional but approachable, and our design language is minimalist as per our Scandinavian heritage.
I will attach our logo as well as some of the graphics we use. Feel free to look at www.brelwickcapital.com.au for more inspiration.
Industry/Entity Type
Finance
Look and feel

```html
<!DOCTYPE html>
<html lang="en">
<head>
<meta charset="utf-8">
<title>Brelwick – Invoice Factoring Brochure</title>
<link rel="stylesheet" href="https://fonts.googleapis.com/css2?family=Didact+Gothic&family=Source+Sans+3:wght@600&display=swap">
<style>
  :root {
    --backdrop: #4d4c4d;
    --paper: #ffffff;
    --heading-blue: #2a6796;
    --body-ink: #1e1e1e;
    --accent-peach: #f2bea4;
    --photo-light: #e6ece8;
    --photo-mid: #b9c7be;
    --photo-deep: #6f8a73;
  }
  * { box-sizing: border-box; margin: 0; padding: 0; }
  html, body { width: 894px; height: 1200px; overflow: hidden; background: var(--backdrop); }
  .page {
    position: absolute; left: 48px; top: 35px; width: 802px; height: 1135px;
    background: var(--paper); overflow: hidden;
  }
  .hero {
    position: absolute; left: 0; top: 0; width: 802px; height: 502px;
    background:
      radial-gradient(ellipse at 50% 55%, #f1ddd6 0%, rgba(241,221,214,0) 35%),
      linear-gradient(100deg, var(--photo-mid) 0%, var(--photo-light) 30%, #f4f2ee 55%, var(--photo-light) 75%, var(--photo-deep) 100%);
  }
  .hero-overlay { position: absolute; left: 0; top: 0; }
  .section-arrow { position: absolute; left: -14px; }
  .heading {
    position: absolute; left: 58px; width: 700px;
    font-family: "Source Sans 3", sans-serif; font-weight: 600;
    font-size: 22.5px; line-height: 25px; color: var(--heading-blue);
  }
  .copy {
    position: absolute; left: 58px; width: 690px;
    font-family: "Didact Gothic", sans-serif; font-size: 13.2px; line-height: 16px;
    color: var(--body-ink);
  }
  .copy p + p { margin-top: 16px; }
  .brand {
    position: absolute; left: 522px; top: 1062px;
    display: flex; align-items: center; gap: 8px;
    font-family: "Source Sans 3", sans-serif; font-weight: 600;
    font-size: 25px; letter-spacing: 1.5px; color: var(--heading-blue);
  }
  .brand-dot { width: 26px; height: 26px; border-radius: 50%; background: var(--heading-blue); }
</style>
</head>
<body>
<main class="page">
  <div class="hero" role="img" aria-label="Photo of a smiling shop owner in an apron holding a blue sign reading Small Business, in front of a bright shopfront"></div>
  <svg class="hero-overlay" width="802" height="502" viewBox="0 0 802 502" aria-hidden="true">
    <ellipse cx="420" cy="250" rx="400" ry="210" fill="none" stroke="#ffffff" stroke-opacity="0.55" stroke-width="28"/>
    <ellipse cx="430" cy="260" rx="360" ry="190" fill="none" stroke="#ffffff" stroke-opacity="0.3" stroke-width="6"/>
    <circle cx="675" cy="485" r="62" fill="none" stroke="var(--accent-peach)" stroke-width="5"/>
    <path d="M636 485 H708 M688 465 L708 485 L688 505" fill="none" stroke="var(--accent-peach)" stroke-width="6" stroke-linecap="round" stroke-linejoin="round"/>
  </svg>

  <svg class="section-arrow" style="top:514px" width="60" height="66" viewBox="0 0 60 66" aria-hidden="true">
    <circle cx="20" cy="33" r="29" fill="none" stroke="var(--accent-peach)" stroke-width="3"/>
    <path d="M4 33 H36 M26 23 L36 33 L26 43" fill="none" stroke="var(--accent-peach)" stroke-width="3" stroke-linecap="round" stroke-linejoin="round"/>
  </svg>
  <h2 class="heading" style="top:533px">Discover the new way to grow your business<br>with the new way to factor your invoices.</h2>
  <div class="copy" style="top:606px">
    <p>You probably spend a lot of your time considering ways to grow your business.</p>
    <p>Cutting costs and increasing prices aren’t always viable options. But injecting additional working capital into your business can increase the number of business cycles and sales you have in a year.</p>
    <p>And the easiest way to access untapped working capital is to get your invoices paid within hours by selling them to Brelwick Finance, the Scandinavian financial services company that’s now operating in Australia.</p>
    <p>While invoice factoring isn’t new, the way that Brelwick lets you factor your invoices is.</p>
  </div>

  <svg class="section-arrow" style="top:791px" width="60" height="66" viewBox="0 0 60 66" aria-hidden="true">
    <circle cx="20" cy="33" r="29" fill="none" stroke="var(--accent-peach)" stroke-width="3"/>
    <path d="M4 33 H36 M26 23 L36 33 L26 43" fill="none" stroke="var(--accent-peach)" stroke-width="3" stroke-linecap="round" stroke-linejoin="round"/>
  </svg>
  <h2 class="heading" style="top:812px">Forget everything you thought you may have heard about<br>about invoice factoring.</h2>
  <div class="copy" style="top:885px">
    <p>The reason more and more companies are finding it attractive to factor their invoices through Brelwick is simple. It’s because we’ve made invoice factoring simple.</p>
    <p>Once you’ve opened an account with Brelwick you can decide which invoices you would like us to buy from you. Within 8 business hours we’ll carry out due diligence to confirm the creditworthiness of your customer and let you know if we will purchase the invoices.</p>
    <p>We’ll buy your 30-day invoices at a 3-6% discount to their face value and you’ll receive the discounted amount within 24 hours. And instead of waiting for a 60-day invoice to be paid, you can sell it to us at a 6-9% discount, again receiving payment in 24 hours.</p>
  </div>

  <div class="brand"><span class="brand-dot"></span>BRELWICK</div>
</main>
</body>
</html>
```